Business cards for start-up accounting firm

I'm looking for a double sided business card ready for upload into Prontel ink or similar print providers with no modification required by me.
I'm looking for something simple as i think cards that are too 'busy' actually detract from the message. I have some thoughts but more than happy to see what comes up. The logo i have came out of left field and i love it the moment i saw it!

My thoughts:

Side 1: Just the logo, perhaps on a dark grey or charcoal background to make the logo colours stand out?

Side 2: The call to action from me website 'Looking for a more relaxed, friendly and interactive relationship with your accountant?' with my contact information
Name: Gavin Ormsby
Email: gavin@quellorix.com.au
Website: www.quellorix.com.au
Phone: 1300 742 916

The call to action needs to be the first thing they see when they look at side 2. If it helps to know what we do and how we do it there is a draft website at www.quellorix.com.au

Like i said, happy to consider anything that comes up :)

Target Market(s)

i'm targeting small business owners who experience a lot of stress around finacial reporting and have had bad experiences with accountants in the past.

Industry/Entity Type

Accounting

Contact Information for Business Card

Contained in the Description

Font styles to use
Serif
Sans Serif
Other font styles liked:
• See logo files attached

Colors
474747

Requirements
Must have
• My logo, slogan and contact information

```html
<!DOCTYPE html>
<html lang="en">
<head>
<meta charset="utf-8">
<title>Quellorix Business Cards</title>
<link href="https://fonts.googleapis.com/css2?family=Open+Sans:wght@400;600;700;800&display=swap" rel="stylesheet">
<style>
  :root {
    --plum: #8b3479;
    --plum-light: #b27aa8;
    --ink: #7a2c6a;
    --paper: #ffffff;
    --stage: #2b2b2b;
  }
  * { box-sizing: border-box; margin: 0; padding: 0; }
  html, body {
    width: 1200px; height: 900px; overflow: hidden;
    background: var(--stage);
    font-family: "Open Sans", Arial, sans-serif;
  }
  .canvas { position: relative; width: 1200px; height: 900px; }
  .card {
    position: absolute; width: 560px; height: 320px;
    border-radius: 18px; overflow: hidden;
  }
  /* Front */
  .card-front { left: 110px; top: 110px; background: var(--plum); color: var(--paper); }
  .front-brand {
    position: absolute; right: 50px; top: 112px; width: 330px; text-align: center;
  }
  .wordmark {
    display: flex; align-items: center; justify-content: center; gap: 10px;
    font-weight: 800; font-size: 50px; letter-spacing: 1px; line-height: 1;
  }
  .wordmark-dot { width: 16px; height: 16px; border-radius: 50%; background: currentColor; }
  .tagline {
    margin-top: 12px; font-size: 12px; letter-spacing: 2px; font-weight: 400;
  }
  .front-web { margin-top: 8px; font-size: 14px; font-weight: 600; letter-spacing: .5px; }

  /* Back */
  .card-back { left: 530px; top: 470px; background: var(--paper); color: var(--ink); }
  .back-art { position: absolute; inset: 0; }
  .back-brand { position: absolute; left: 30px; top: 52px; width: 230px; }
  .back-brand .wordmark { justify-content: flex-start; font-size: 34px; color: var(--plum); gap: 8px; }
  .back-brand .wordmark-dot { width: 11px; height: 11px; }
  .back-brand .tagline { font-size: 8px; letter-spacing: 1.5px; margin-top: 7px; color: var(--plum); }
  .holder {
    position: absolute; left: 30px; top: 138px;
    font-size: 20px; font-weight: 700; letter-spacing: .5px; color: var(--ink);
  }
  .contacts { position: absolute; left: 30px; top: 180px; list-style: none; font-size: 12.5px; line-height: 18px; }
  .contacts li { display: flex; align-items: center; gap: 8px; }
  .contacts svg { width: 11px; height: 11px; flex: none; }
  .cta {
    position: absolute; left: 30px; top: 242px; width: 290px;
    font-size: 10.5px; font-weight: 600; line-height: 14px; text-transform: uppercase; color: var(--ink);
  }
</style>
</head>
<body>
<main class="canvas">
  <section class="card card-front" aria-label="Card front">
    <div class="front-brand">
      <div class="wordmark"><span>QUELLORIX</span><span class="wordmark-dot"></span></div>
      <div class="tagline">CALM BOOKS, CLEAR GROWTH</div>
      <div class="front-web">www.quellorix.com.au</div>
    </div>
  </section>

  <section class="card card-back" aria-label="Card back">
    <svg class="back-art" viewBox="0 0 560 320" preserveAspectRatio="none" aria-hidden="true">
      <line x1="30" y1="170" x2="230" y2="170" stroke="#8b3479" stroke-width="2.5"/>
      <line x1="230" y1="170" x2="560" y2="88" stroke="#8b3479" stroke-width="1.2"/>
      <path d="M0,302 C200,300 340,288 430,228 C490,186 530,150 560,132 L560,320 L0,320 Z" fill="#b27aa8"/>
      <path d="M0,312 C200,312 350,300 440,240 C495,202 532,166 560,150 L560,320 L0,320 Z" fill="#ffffff"/>
      <path d="M0,318 C210,318 360,306 448,248 C500,212 534,178 560,164 L560,320 L0,320 Z" fill="#8b3479"/>
    </svg>
    <div class="back-brand">
      <div class="wordmark"><span>QUELLORIX</span><span class="wordmark-dot"></span></div>
      <div class="tagline">CALM BOOKS, CLEAR GROWTH</div>
    </div>
    <h1 class="holder">GAVIN ORMSBY</h1>
    <ul class="contacts">
      <li><svg viewBox="0 0 24 24"><path d="M6.6 10.8a15 15 0 0 0 6.6 6.6l2.2-2.2a1 1 0 0 1 1-.25 11.4 11.4 0 0 0 3.6.57 1 1 0 0 1 1 1V20a1 1 0 0 1-1 1A17 17 0 0 1 3 4a1 1 0 0 1 1-1h3.5a1 1 0 0 1 1 1c0 1.250.2 2.45.57 3.57a1 1 0 0 1-.25 1z" fill="#7a2c6a"/></svg>1300 742 916</li>
      <li><svg viewBox="0 0 24 24"><rect x="2" y="5" width="20" height="14" rx="2" fill="none" stroke="#7a2c6a" stroke-width="2"/><path d="M2 6l10 7 10-7" fill="none" stroke="#7a2c6a" stroke-width="2"/></svg>gavin@quellorix.com.au</li>
      <li><svg viewBox="0 0 24 24"><circle cx="12" cy="12" r="9.5" fill="none" stroke="#7a2c6a" stroke-width="2"/><path d="M2.5 12h19M12 2.5c3 3 3 16 0 19M12 2.5c-3 3-3 16 0 19" fill="none" stroke="#7a2c6a" stroke-width="1.6"/></svg>www.quellorix.com.au</li>
    </ul>
    <p class="cta">Looking for a more relaxed, friendly and interactive relationship with your accountant</p>
  </section>
</main>
</body>
</html>
```